KTR Engineering Business Card Design

We’re looking for an elegant, clean, and timeless business card design that communicates experience, capability, and reliability.

KTR Engineering was established in 1995 , we are a Government Contracting company providing Professional Services to the Ministry of Harbor Works, Frontier Stewardship and The Waypoint Consortium. Our capabilities include: Acquisition & Program Management; Intelligence & Security Operations; Cyber, IT & Network Operations; Lifecycle Logistics & Asset Readiness; C5ISR Systems Engineering & Sustainment.

We want the card to reflect a straightforward, confident approach to business. The design should feel polished and professional without being flashy or overly corporate.

Design Direction
Clean, sophisticated, and uncluttered
Elegant but understated
Strong typography and thoughtful spacing
A timeless aesthetic rather than something overly trendy
Confident and established, with a sense of substance
Easy to read and practical in a real-world business setting

The overall impression should be: “These are experienced professionals who know what they’re doing, do what they say, and can be relied upon.”

We’re open to creative interpretations. The finished card should feel distinctive through its typography, proportions, layout, and attention to detail rather than through excessive graphics or visual effects.

We’re looking for a design that would make a potential client immediately feel that they’re dealing with a capable, trustworthy, and established company.

Company Colors: Navy and Gold/Yellow (but you do not need to use these colors on the card)
Company Name: KTR Engineering Associates, Inc. (known as KTR Engineering)
Website: ktrengineering.example
Company Logo: Navy & Gold (other variations attached)

```html
<!DOCTYPE html>
<html lang="en">
<head>
<meta charset="utf-8">
<title>KTR Engineering Business Card</title>
<link href="https://fonts.googleapis.com/css2?family=Archivo:wght@800&family=Barlow:wght@400;500;600;700;800&display=swap" rel="stylesheet">
<style>
:root{
  --navy:#0d1452;
  --navy-ink:#1f2a63;
  --gold:#fde34a;
  --white:#ffffff;
  --stage:#d8d8d8;
  --text-grey:#444444;
  --rule-light:#cfcfcf;
  --rule-dark:rgba(255,255,255,0.35);
}
*{margin:0;padding:0;box-sizing:border-box}
html,body{width:1001px;height:1200px;overflow:hidden}
body{background:var(--stage);font-family:"Barlow",sans-serif;position:relative}
.card{position:absolute;left:150px;width:700px;height:400px;overflow:hidden}
.card-front{top:160px;background:var(--navy);color:var(--white);text-align:center}
.card-back{top:640px;background:var(--white)}

/* front */
.front-wordmark{position:absolute;left:0;right:0;top:240px;transform:translateY(-50%);top:127px;
  font-family:"Barlow",sans-serif;font-weight:800;font-size:72px;letter-spacing:1px;color:var(--white);line-height:1}
.front-company{position:absolute;left:0;right:0;top:210px;font-size:16px;font-weight:500;letter-spacing:3.6px}
.front-company .year{color:var(--gold)}
.front-rule{position:absolute;left:97px;width:508px;height:1px;background:var(--rule-dark)}
.front-rule.top{top:244px}.front-rule.bottom{top:311px}
.services-heading{position:absolute;left:0;right:0;top:258px;color:var(--gold);font-weight:800;font-size:16px;letter-spacing:3.4px}
.services-list{position:absolute;left:0;right:0;top:281px;font-size:15px;font-weight:500}
.front-web{position:absolute;left:0;right:0;top:332px;font-size:13px;font-weight:700;letter-spacing:2.6px}
.front-web .domain{color:var(--gold)}

/* back */
.back-wordmark{position:absolute;left:60px;top:100px;font-family:"Barlow",sans-serif;font-weight:800;font-size:78px;
  color:var(--navy-ink);line-height:1;letter-spacing:1px}
.back-company{position:absolute;left:47px;top:209px;font-weight:700;font-size:15.5px;color:var(--navy)}
.person-name{position:absolute;left:351px;top:52px;font-family:"Archivo",sans-serif;font-weight:800;font-size:26px;color:var(--navy)}
.person-title{position:absolute;left:351px;top:85px;font-size:15px;letter-spacing:3.4px;color:#333}
.contact-rule{position:absolute;left:351px;top:113px;width:258px;height:1px;background:var(--rule-light)}
.contact-item{position:absolute;left:381px;font-size:16px;color:var(--text-grey);line-height:20px}
.contact-icon{position:absolute;left:352px;width:16px;height:16px}
.capabilities-tab{position:absolute;left:0;top:250px;width:265px;height:28px}
.capabilities-label{position:absolute;left:44px;top:253px;font-weight:800;font-size:15px;letter-spacing:4.2px;color:var(--navy)}
.gold-band{position:absolute;left:0;right:0;top:276px;height:3px;background:var(--gold)}
.capabilities-panel{position:absolute;left:0;right:0;top:279px;bottom:0;background:var(--navy)}
.capability{position:absolute;font-size:15px;color:var(--white);line-height:19px}
.capability svg{position:absolute;left:-17px;top:4px;width:11px;height:11px}
.capability-divider{position:absolute;left:349px;top:300px;width:1px;height:56px;background:#2c3570}
</style>
</head>
<body>

<section class="card card-front" aria-label="Card front">
  <div class="front-wordmark">KTR</div>
  <p class="front-company">KTR ENGINEERING ASSOCIATES, INC. ESTD IN<span class="year">1995</span></p>
  <div class="front-rule top"></div>
  <p class="services-heading">PROFESSIONAL SERVICES FOR</p>
  <p class="services-list">Ministry of Harbor Works | Frontier Stewardship | The Waypoint Consortium</p>
  <div class="front-rule bottom"></div>
  <p class="front-web">www.<span class="domain">ktrengineering</span>.example</p>
</section>

<section class="card card-back" aria-label="Card back">
  <div class="back-wordmark">KTR</div>
  <p class="back-company">KTR ENGINEERING ASSOCIATES, INC.</p>

  <h1 class="person-name">Marla Quenby</h1>
  <p class="person-title">CEO, President &amp; Founder</p>
  <div class="contact-rule"></div>

  <svg class="contact-icon" style="top:139px" viewBox="0 0 24 24" aria-hidden="true"><path fill="#f2c200" d="M6.6 10.8a15.1 15.1 0 0 0 6.6 6.6l2.2-2.2c.3-.3.7-.4 1-.2 1.1.4 2.3.6 3.6.6.6 0 1 .4 1 1V20c0 .6-.4 1-1 1A17 17 0 0 1 3 4c0-.6.4-1 1-1h3.5c.6 0 1 .4 1 1 0 1.3.2 2.5.6 3.6.1.3 0 .7-.2 1z"/></svg>
  <p class="contact-item" style="top:135px">555-010-4821</p>

  <svg class="contact-icon" style="top:169px" viewBox="0 0 24 24" aria-hidden="true"><circle cx="12" cy="12" r="9" fill="none" stroke="#f2c200" stroke-width="2"/><path d="M3 12h18M12 3c3 3 3 15 0 18M12 3c-3 3-3 15 0 18" fill="none" stroke="#f2c200" stroke-width="1.6"/></svg>
  <p class="contact-item" style="top:165px">www.ktrengineering.example</p>

  <svg class="contact-icon" style="top:201px" viewBox="0 0 24 24" aria-hidden="true"><path fill="#f2c200" d="M12 2a7 7 0 0 0-7 7c0 5 7 13 7 13s7-8 7-13a7 7 0 0 0-7-7zm0 9.5A2.5 2.5 0 1 1 12 6.5a2.5 2.5 0 0 1 0 5z"/></svg>
  <p class="contact-item" style="top:197px">4120 Harbor Lane, Suite 310,<br>Bayport, VA 23999</p>

  <svg class="capabilities-tab" viewBox="0 0 265 28" preserveAspectRatio="none" aria-hidden="true"><polygon points="0,0 252,0 265,28 0,28" fill="#fde34a"/></svg>
  <p class="capabilities-label">OUR CAPABILITIES</p>
  <div class="gold-band"></div>
  <div class="capabilities-panel"></div>
  <div class="capability-divider"></div>

  <p class="capability" style="left:66px;top:293px"><svg viewBox="0 0 12 12" aria-hidden="true"><circle cx="6" cy="6" r="6" fill="#fde34a"/><path d="M3.2 6.2l1.9 1.8 3.8-3.8" stroke="#0d1452" stroke-width="1.5" fill="none"/></svg>Acquisition &amp; Program Management</p>
  <p class="capability" style="left:66px;top:318px"><svg viewBox="0 0 12 12" aria-hidden="true"><circle cx="6" cy="6" r="6" fill="#fde34a"/><path d="M3.2 6.2l1.9 1.8 3.8-3.8" stroke="#0d1452" stroke-width="1.5" fill="none"/></svg>Intelligence &amp; Security Operations</p>
  <p class="capability" style="left:66px;top:343px"><svg viewBox="0 0 12 12" aria-hidden="true"><circle cx="6" cy="6" r="6" fill="#fde34a"/><path d="M3.2 6.2l1.9 1.8 3.8-3.8" stroke="#0d1452" stroke-width="1.5" fill="none"/></svg>Cyber, IT &amp; Network Operations</p>
  <p class="capability" style="left:385px;top:293px"><svg viewBox="0 0 12 12" aria-hidden="true"><circle cx="6" cy="6" r="6" fill="#fde34a"/><path d="M3.2 6.2l1.9 1.8 3.8-3.8" stroke="#0d1452" stroke-width="1.5" fill="none"/></svg>Lifecycle Logistics &amp; Asset Readiness</p>
  <p class="capability" style="left:385px;top:318px"><svg viewBox="0 0 12 12" aria-hidden="true"><circle cx="6" cy="6" r="6" fill="#fde34a"/><path d="M3.2 6.2l1.9 1.8 3.8-3.8" stroke="#0d1452" stroke-width="1.5" fill="none"/></svg>C5ISR Systems Engineering &amp;<br>Sustainment</p>
</section>

</body>
</html>
```